Redesign Website for Corvane Blaze

I have an existing website on https://www.corvaneblaze-demo.com.au/ and would like to have this redesigned professionally with new content (please refer to word document). We are fire protection engineers providing fire services design expertise and engineering design to a range of different clients.

We also provide drafting services to clients in the form of completing final commissioning documentation such as 'as-installed' drawings and fire services block plans to ensure compliance with the building code and relevant Australian Standards.

Target Market(s)

Builders, Architects, Consultants, Project Managers

Industry/Entity Type

Engineering Consultant

Coding

Coded - Design and coding required

Number of Pages Required

4 page

Font styles to use
Sans Serif

Requirements
Must have
• Home and about Page, fire services design page, fire block plans page, contact us page (4 Pages).

The website colour choice must match or compliment the new company logo.
Nice to have
• Quality photos of fire services installations in buildings to Australian Standards.

A website similar to this would be ideal http://quorbelflame-demo.com.au
Should not have
• Stolen licensed photos

```html
<!DOCTYPE html>
<html lang="en">
<head>
<meta charset="utf-8">
<title>Fire Block Plans – Corvane Blaze</title>
<link href="https://fonts.googleapis.com/css2?family=Bebas+Neue&family=Montserrat:wght@500;600&family=Poppins:wght@300;400;500&display=swap" rel="stylesheet">
<style>
:root{
  --orange:#f39325;
  --grey:#8c8c8c;
  --text:#444;
  --dark:#444444;
  --dark-2:#3a3a3a;
  --white:#fff;
}
*{box-sizing:border-box;margin:0;padding:0}
html,body{width:756px;height:1200px;overflow:hidden;background:var(--white)}
body{position:relative;font-family:"Poppins",sans-serif;color:var(--text)}
.abs{position:absolute}
.hero-art{position:absolute;left:0;top:0}
.brand{left:102px;top:28px;font-family:"Poppins",sans-serif;font-weight:500;font-size:15px;color:var(--orange);letter-spacing:.5px}
.nav{top:31px;left:343px;display:flex;gap:13px;font-size:8.8px;color:var(--white);letter-spacing:.1px}
.nav .active{color:var(--orange)}
.headline{left:102px;top:114px;font-family:"Bebas Neue",sans-serif;font-size:28px;line-height:26px;color:var(--orange);letter-spacing:.4px}
.tagline{left:102px;top:173px;font-family:"Montserrat",sans-serif;font-weight:600;font-size:10.6px;line-height:14.5px;color:var(--grey)}
.btn-call{left:102px;top:227px;width:87px;height:26px;background:var(--orange);color:var(--white);font-family:"Montserrat",sans-serif;font-weight:600;font-size:8.3px;display:flex;align-items:center;justify-content:center}
.crumbs{left:102px;top:318px;font-size:8.4px;color:var(--text)}
.crumbs .sep{margin:0 6px}
.crumbs .current{color:var(--orange);font-family:"Montserrat",sans-serif;font-weight:500}
.page-title{left:0;width:756px;top:370px;text-align:center;font-family:"Montserrat",sans-serif;font-weight:600;font-size:22px;color:var(--grey);letter-spacing:.6px}
.page-title span{color:var(--orange)}
.title-rule{left:366px;top:403px;width:24px;height:1px;background:var(--grey)}
.intro{left:120px;width:516px;top:421px;text-align:center;font-size:8.8px;line-height:15.5px;color:var(--text)}
.plan-title{font-size:11px;font-weight:400;color:#333}
.plan-body{font-size:7.7px;line-height:12.9px;font-weight:300;color:#333}
.left{text-align:left}
.right{text-align:right}
.btn-contact{left:315px;top:810px;width:126px;height:24px;border:1.3px solid var(--orange);display:flex;align-items:center;justify-content:center;font-family:"Montserrat",sans-serif;font-weight:500;font-size:9px;color:#555;letter-spacing:.4px}
.footer-brand{left:0;width:756px;top:982px;text-align:center;font-weight:500;font-size:20px;color:var(--orange);letter-spacing:.5px}
.contact-item{width:200px;text-align:center;color:var(--white)}
.contact-item h3{font-family:"Montserrat",sans-serif;font-weight:500;font-size:9.4px;margin-bottom:6px}
.contact-item p{font-size:9px;line-height:15px;font-weight:300}
.footer-rule{left:0;top:1166px;width:756px;height:1px;background:#5a5a5a}
.legal{top:1178px;font-size:8.6px;font-weight:300;color:var(--white)}
</style>
</head>
<body>

<svg class="hero-art" width="756" height="1200" viewBox="0 0 756 1200">
  <defs>
    <linearGradient id="carpark" x1="0" y1="0" x2="0" y2="1">
      <stop offset="0" stop-color="#6e6c66"/>
      <stop offset=".55" stop-color="#a5a49e"/>
      <stop offset="1" stop-color="#8c8a84"/>
    </linearGradient>
    <linearGradient id="corridor" x1="0" y1="0" x2="1" y2="0">
      <stop offset="0" stop-color="#c8c4bc"/>
      <stop offset=".6" stop-color="#e6e2da"/>
      <stop offset="1" stop-color="#2c2d30"/>
    </linearGradient>
  </defs>
  <polygon points="314,0 756,0 756,302 460,236 352,196" fill="url(#carpark)" role="img" aria-label="Photo of an underground car park with fire services and an exit sign"/>
  <polyline points="460,238 728,340 756,327" fill="none" stroke="var(--orange)" stroke-width="1"/>
  <polygon points="368,183 432,183 462,236 432,289 368,289 338,236" fill="var(--white)" stroke="var(--orange)" stroke-width="1.2"/>
  <polygon points="373,190 427,190 455,236 427,284 373,284 345,236" fill="url(#corridor)" role="img" aria-label="Photo of a building corridor during fit-out"/>
  <polygon points="545,14 552,14 555,20 552,26 545,26 542,20" fill="none" stroke="var(--orange)" stroke-width="1"/>

  <!-- block plan diagram -->
  <g fill="none" stroke="var(--orange)" stroke-width="1">
    <polygon points="318,578 346,526 409,526 438,578 409,630 346,630"/>
    <polyline points="346,526 328,494 155,494"/>
    <polyline points="409,526 427,494 600,494"/>
    <polyline points="346,630 328,661 155,661"/>
    <polyline points="409,630 427,661 600,661"/>
    <line x1="103" y1="494" x2="110" y2="494"/>
    <line x1="646" y1="494" x2="652" y2="494"/>
    <line x1="103" y1="661" x2="110" y2="661"/>
    <line x1="646" y1="661" x2="652" y2="661"/>
    <polygon points="121,474 143,474 155,494 143,514 121,514 110,494"/>
    <polygon points="612,474 634,474 646,494 634,514 612,514 600,494"/>
    <polygon points="121,641 143,641 155,661 143,681 121,681 110,661"/>
    <polygon points="612,641 634,641 646,661 634,681 612,681 600,661"/>
    <g fill="var(--white)">
      <circle cx="346" cy="526" r="4"/><circle cx="409" cy="526" r="4"/>
      <circle cx="346" cy="630" r="4"/><circle cx="409" cy="630" r="4"/>
    </g>
  </g>
  <g fill="var(--orange)">
    <circle cx="103" cy="494" r="2"/><circle cx="652" cy="494" r="2"/>
    <circle cx="103" cy="661" r="2"/><circle cx="652" cy="661" r="2"/>
    <circle cx="346" cy="526" r="1.6"/><circle cx="409" cy="526" r="1.6"/>
    <circle cx="346" cy="630" r="1.6"/><circle cx="409" cy="630" r="1.6"/>
  </g>
  <g fill="#fbe3c6">
    <rect x="122" y="484" width="20" height="20" role="img" aria-label="Sprinkler head icon"/>
    <rect x="613" y="484" width="20" height="20" role="img" aria-label="Floor plan icon"/>
    <rect x="122" y="651" width="20" height="20" role="img" aria-label="Fire hydrant icon"/>
    <rect x="613" y="651" width="20" height="20" role="img" aria-label="Drafting plan icon"/>
  </g>
  <text x="378" y="581" text-anchor="middle" font-family="Poppins, sans-serif" font-weight="500" font-size="9" fill="var(--orange)">Corvane Blaze</text>

  <!-- footer -->
  <polygon points="0,975 378,893 756,975 756,1200 0,1200" fill="var(--dark)"/>
  <g fill="var(--dark-2)" stroke="#4f4f4f" stroke-width="1">
    <polygon points="178,1037 198,1037 208,1055 198,1073 178,1073 168,1055"/>
    <polygon points="367,1035 389,1035 400,1055 389,1075 367,1075 356,1055"/>
    <polygon points="564,1037 584,1037 594,1055 584,1073 564,1073 554,1055"/>
  </g>
  <g fill="var(--orange)">
    <path d="M183,1049c1-1 2-1 2.5,0l1.5,2c.5,.8 .2,1.4-.5,2l-.8,.7c.7,1.6 2,2.9 3.6,3.6l.7-.8c.6-.7 1.2-1 2-.5l2,1.5c1,.5 1,1.5 0,2.5l-1,1c-4,1-11-6-10-10z"/>
    <path d="M378,1046c-3.8,0-6,2.6-6,5.6 0,4 6,11 6,11s6-7 6-11c0-3-2.2-5.6-6-5.6zm0,8a2.4,2.4 0 1 1 0-4.8a2.4,2.4 0 0 1 0,4.8z"/>
    <rect x="568" y="1050" width="12" height="9" rx="1"/>
  </g>
  <polyline points="568,1051 574,1055.5 580,1051" fill="none" stroke="var(--dark-2)" stroke-width="1"/>
</svg>

<div class="abs brand">CORVANE BLAZE</div>
<nav class="abs nav">
  <span>ABOUT US</span><span>FIRE SERVICES DESIGN</span><span class="active">FIRE BLOCK PLANS</span><span>CONTACT US</span>
</nav>

<h1 class="abs headline">WE ARE FIRE<br>PROTECTION ENGINEERS</h1>
<p class="abs tagline">PROVIDING FIRE SERVICES DESIGN<br>EXPERTISE AND ENGINEERING DESIGN<br>TO A RANGE OF DIFFERENT CLIENTS.</p>
<div class="abs btn-call">CALL US TODAY</div>

<div class="abs crumbs">HOME<span class="sep">/</span><span class="current">FIRE BLOCK PLANS</span></div>

<h2 class="abs page-title">FIRE <span>BLOCK PLANS</span></h2>
<div class="abs title-rule"></div>
<p class="abs intro">We can also assist our clients in the preparation of final commissioning documentation as required for relevant fire safety systems to achieve full compliance with relevant Australian Standards.</p>

<h3 class="abs plan-title left" style="left:161px;top:476px">Sprinkler Block Plan</h3>
<p class="abs plan-body left" style="left:164px;top:502px;width:160px">AS2118.1 requires each sprinkler installation to be provided with a plan of the protected building(s) with the position of main stop valves clearly indicated adjacent to each set or group of installation control assemblies where it can be readily seen by firefighters and others responding to the alarm.</p>

<h3 class="abs plan-title right" style="left:440px;width:148px;top:476px">Zone Block Plan</h3>
<p class="abs plan-body right" style="left:430px;width:162px;top:502px">AS1670.1 requires a zone block plan of an automatic smoke detection and alarm system installation to be securely mounted and easily accessible at the fire brigade panel. The plan shall be in the form of a permanent diagram that is water resistant and fade resistant.</p>

<h3 class="abs plan-title left" style="left:161px;top:637px">Hydrant Block Plan</h3>
<p class="abs plan-body left" style="left:164px;top:670px;width:160px">AS2419.1 requires a hydrant block plan (minimum A3 size) to be fixed within the booster cabinet, enclosure, recess, fire control room and pump room where it can be readily seen by firefighters and others responding to the alarm.</p>

<h3 class="abs plan-title right" style="left:400px;width:192px;top:639px">Emergency Zone Block Plan</h3>
<p class="abs plan-body right" style="left:428px;width:164px;top:670px">AS1670.4 requires an emergency zone block plan of the installed emergency warning &amp; intercom system to be securely mounted and easily accessible at the EWCIE. The emergency zone block plan shall cover the area served by the particular emergency warning &amp; intercom systems to be securely mounted and easily accessible at the EWCIE.</p>

<div class="abs btn-contact">CONTACT US TODAY</div>

<div class="abs footer-brand">CORVANE BLAZE</div>

<div class="abs contact-item" style="left:88px;top:1087px"><h3>PHONE</h3><p>+614 55 210 374</p></div>
<div class="abs contact-item" style="left:278px;top:1087px"><h3>ADDRESS</h3><p>PO Box 412<br>Marrowdale, NSW 2199</p></div>
<div class="abs contact-item" style="left:474px;top:1087px"><h3>EMAIL</h3><p>info@corvaneblaze-demo.com.au</p></div>

<div class="abs footer-rule"></div>
<p class="abs legal" style="left:103px">Copyright © 2021 Corvane Blaze. All Rights Reserved.</p>
<p class="abs legal" style="right:103px">ABN: 52 904 117 386</p>

</body>
</html>
```